Ironbark Shift Workforce

We are a underground coal mining labour hire company, needing a website that links into our online payroll (www.wagetrackly.com.au) and also need to have job applications page that is a preform with drop down menu,s with answers or check boxes. We would also need a 3 tier administration access for access to different files.
We are looking for an ongoing relationship with future app integration

Reason: There are a few more designs to come and I'm out at the mine for another week

Industry/Entity Type

Coal Mining

```html
<!DOCTYPE html>
<html lang="en">
<head>
<meta charset="utf-8">
<title>Ironbark Shift Workforce</title>
<link rel="stylesheet" href="https://fonts.googleapis.com/css2?family=Open+Sans:wght@300;400;600;700&display=swap">
<style>
:root{
  --orange:#f47b20;
  --orange-dark:#e0661a;
  --ink:#0c0c14;
  --black:#050507;
  --white:#ffffff;
  --grey-text:#5a5a5a;
  --grey-light:#9a9a9a;
  --rule:#e2e2e2;
  --card:#f3f3f3;
}
*{box-sizing:border-box;margin:0;padding:0}
html,body{width:1200px;height:3529px;overflow:hidden}
body{font-family:"Open Sans",Arial,sans-serif;color:var(--grey-text);background:var(--white);position:relative}
section,header,footer,div,p,span,a,h1,h2,h3,h4,ul,li{position:relative}
a{color:inherit;text-decoration:none}
ul{list-style:none}
.abs{position:absolute}
.accent{color:var(--orange)}

/* top bar */
.topbar{height:33px;background:var(--black);color:#ddd;font-size:11px;display:flex;align-items:center;gap:26px;padding-left:72px}
.topbar span{display:flex;align-items:center;gap:6px}

/* nav */
.nav{height:99px;background:var(--black)}
.brand{position:absolute;left:88px;top:24px;display:flex;align-items:center;gap:12px;color:var(--white);font-weight:700;font-size:30px;letter-spacing:1px}
.brand-dot{width:50px;height:50px;border-radius:50%;background:var(--white)}
.menu{position:absolute;left:395px;top:53px;display:flex;gap:0;font-size:12px;color:var(--white);font-weight:600}
.menu a{margin-right:34px}
.menu a.active{color:var(--orange)}
.search{position:absolute;left:1110px;top:52px}

/* hero */
.hero{height:400px;background:radial-gradient(ellipse at 85% 70%,#f4b13a 0%,#c0551b 22%,#6a2f16 48%,#2a1a12 80%)}
.hero-title{position:absolute;left:0;right:0;top:60px;text-align:center;color:var(--white);font-weight:300;font-size:84px;line-height:86px;letter-spacing:8px}
.hero-title small{font-size:58px;letter-spacing:4px}
.hero-sub{position:absolute;left:0;right:0;top:242px;text-align:center;color:var(--white);font-weight:700;font-size:17px}
.btn{display:inline-block;background:var(--orange);color:var(--white);font-weight:700;font-size:11px;text-align:center}
.hero-btn{position:absolute;left:510px;top:298px;width:196px;height:38px;line-height:34px;border:2px solid #fff2;letter-spacing:1px}

/* intro */
.intro{height:174px;text-align:center;padding-top:40px;font-size:20px;line-height:29px;letter-spacing:2px;color:var(--grey-text);text-transform:uppercase}

/* services */
.services{height:310px;background:var(--ink);color:var(--white)}
.svc{position:absolute;top:60px;width:190px;text-align:center}
.svc h3{font-size:14px;font-weight:400;margin-top:22px;line-height:19px}
.svc .more{font-size:10px;color:var(--orange);margin-top:6px;display:block}
.hr-block{position:absolute;left:678px;top:48px;width:452px}
.hr-block .kicker{color:var(--orange);font-size:13px;font-weight:600}
.hr-block h2{color:var(--orange);font-size:50px;font-weight:300;line-height:62px}
.hr-block p{font-size:12px;line-height:17px;margin-top:6px}

/* what we do */
.what{height:438px}
.section-title{position:absolute;left:0;right:0;text-align:center;font-weight:300;color:var(--grey-text)}
.what .section-title{top:36px;font-size:40px;letter-spacing:1px}
.what .sub{position:absolute;left:0;right:0;top:92px;text-align:center;font-size:14px;color:var(--grey-light)}
.badge-art{position:absolute;left:165px;top:125px;width:247px;height:235px;background:radial-gradient(circle,#e5832f 0%,#3a3a3a 55%,#ffffff 72%)}
.what-text{position:absolute;left:617px;top:142px;width:500px;font-size:12px;line-height:17px}
.features{position:absolute;top:200px;width:240px;font-size:12px}
.features li{height:36px;line-height:36px;border-bottom:1px solid var(--rule);padding-left:16px}
.features li::before{content:"";position:absolute;left:2px;top:15px;border-left:5px solid var(--orange);border-top:4px solid transparent;border-bottom:4px solid transparent}
.what .btn{position:absolute;top:376px;height:32px;line-height:32px}

/* projects */
.projects{height:574px;background:var(--ink);color:var(--white)}
.projects .section-title{top:40px;font-size:42px;color:var(--orange)}
.projects .sub{position:absolute;left:0;right:0;top:96px;text-align:center;color:var(--orange);font-weight:700;font-size:15px}
.projects .lede{position:absolute;left:200px;width:800px;top:146px;text-align:center;font-size:12px;line-height:18px}
.cards{position:absolute;left:70px;top:221px;width:1060px;display:flex;gap:4px}
.card{width:262px;background:var(--card)}
.card .photo{height:176px}
.card h4{color:#333;font-weight:400;font-size:15px;text-align:center;line-height:20px;padding-top:14px}
.card .links{text-align:center;font-size:11px;color:var(--orange);margin-top:8px;padding-bottom:18px}
.dots{position:absolute;left:0;right:0;top:514px;display:flex;justify-content:center;gap:9px}
.dots i{width:8px;height:8px;border-radius:50%;background:var(--white)}
.dots i:first-child{background:var(--orange)}

/* clients */
.clients{height:400px}
.clients .section-title{top:40px;font-size:40px}
.clients .sub{position:absolute;left:0;right:0;top:94px;text-align:center;font-size:15px;color:var(--grey-light);letter-spacing:.5px}
.arrow{position:absolute;top:168px;width:45px;height:45px}
.logos{position:absolute;left:150px;top:170px;width:900px;display:flex;justify-content:space-around;align-items:center;height:42px}
.logos span{display:flex;align-items:center;gap:7px;font-size:19px;font-weight:600;color:#2c5d9a}
.logos span i{width:18px;height:18px;border-radius:50%;background:var(--orange)}
.quote{position:absolute;left:230px;width:740px;top:252px;text-align:center;font-size:12px;line-height:19px}
.author{position:absolute;left:508px;top:312px;display:flex;align-items:center;gap:16px}
.avatar{width:54px;height:54px;border-radius:50%;background:linear-gradient(#8b8b8b,#d9d9d9)}
.author b{display:block;color:var(--orange);font-size:16px;font-weight:400}
.author small{font-size:10px;color:var(--grey-light)}

/* team */
.team{height:572px;background:var(--ink);color:var(--white)}
.team .kicker{position:absolute;left:0;right:0;top:40px;text-align:center;color:var(--orange);font-size:12px;font-weight:600}
.team .section-title{top:54px;font-size:42px;color:var(--orange)}
.member{position:absolute;top:138px;width:240px;text-align:center}
.member .portrait{width:200px;height:200px;border-radius:50%;margin:0 auto;border:4px solid #e8e8e8;background:radial-gradient(circle at 50% 40%,#c9a58a,#8a8a8a 70%)}
.member h4{font-size:15px;font-weight:700;margin-top:28px}
.member .role{font-size:11px;font-style:italic;margin-top:2px}
.member p{font-size:12px;line-height:17px;margin-top:8px}
.social{display:flex;justify-content:center;gap:7px;margin-top:16px}
.social i{width:21px;height:21px;border-radius:50%;background:#dcdcdc}
.social i.on{background:var(--orange)}

/* footer */
.footer{height:395px}
.foot-brand{position:absolute;left:82px;top:94px;display:flex;align-items:center;gap:10px;font-size:34px;font-weight:700;color:#8a8a8a}
.foot-brand i{width:46px;height:46px;border-radius:50%;background:#9a9a9a}
.foot-about{position:absolute;left:82px;top:160px;width:200px;font-size:12px;line-height:17px}
.foot-about .btn,.contact .btn{height:30px;line-height:30px}
.col{position:absolute;top:54px}
.col h4{font-size:15px;font-weight:400;color:#444;margin-bottom:18px}
.tweet{display:flex;gap:12px;width:240px;font-size:12px;line-height:16px;margin-bottom:22px}
.tweet i{flex:none;width:20px;height:20px;border-radius:50%;background:var(--orange)}
.tweet a{display:block;color:var(--orange);font-style:italic;font-size:11px;margin-top:10px;text-decoration:underline}
.links li{width:195px;height:36px;line-height:36px;border-bottom:1px solid var(--rule);font-size:12px;padding-left:14px}
.links li::before{content:"";position:absolute;left:1px;top:16px;width:5px;height:5px;border-radius:50%;background:var(--orange)}
.links li.active{color:var(--orange)}
.contact p{font-size:12px;line-height:18px;margin-bottom:14px}

/* bottom */
.bottom{height:134px;background:var(--black);color:var(--white);font-size:11px}
.copy{position:absolute;left:87px;top:62px}
.bottom-links a{position:absolute;top:62px}
.to-top{position:absolute;left:579px;top:101px;width:44px;height:33px;background:var(--orange)}
</style>
</head>
<body>

<div class="topbar">
  <span><svg width="10" height="13" viewBox="0 0 10 13"><path d="M5 0a5 5 0 0 1 5 5c0 3.5-5 8-5 8S0 8.5 0 5a5 5 0 0 1 5-5z" fill="#f47b20"/><circle cx="5" cy="5" r="2" fill="#050507"/></svg>42 Seam Road, Moranbah QLD 4744</span>
  <span><svg width="12" height="12" viewBox="0 0 12 12"><path d="M2 0l3 3-1.5 1.8a8 8 0 0 0 3.7 3.7L9 7l3 3-2 2C5 12 0 7 0 2z" fill="#f47b20"/></svg>+61 7 4941 2208</span>
  <span><svg width="14" height="10" viewBox="0 0 14 10"><rect width="14" height="10" rx="1" fill="#f47b20"/><path d="M1 1l6 5 6-5" stroke="#050507" fill="none"/></svg>hello@ironbarkshift.com.au</span>
</div>

<header class="nav">
  <div class="brand"><i class="brand-dot"></i>ISW</div>
  <nav class="menu">
    <a class="active">HOME</a><a>ABOUT</a><a>SERVICES</a><a>APPLICANTS</a><a>SITES</a><a>TEAM</a><a>NEWS</a><a>LOGIN</a><a>CONTACT</a>
  </nav>
  <svg class="search" width="14" height="14" viewBox="0 0 14 14"><circle cx="6" cy="6" r="4.5" stroke="#f47b20" stroke-width="1.6" fill="none"/><path d="M9.5 9.5L13 13" stroke="#f47b20" stroke-width="1.8"/></svg>
</header>

<section class="hero" role="img" aria-label="Photo of an arched underground mine tunnel lit in warm orange light">
  <h1 class="hero-title">WE KEEP <small>IT</small><br>WORKING</h1>
  <p class="hero-sub">Lorem ipsum dolor sit amet, consectetuer adipiscing elit.</p>
  <a class="btn hero-btn">KNOW &nbsp; MORE</a>
</section>

<section class="intro">
  Lorem ipsum dolor sit amet, <span class="accent">consectetuer adipiscing</span> elit.<br>
  Aenean commodo ligula eget dolor. Aenean massa. Cum<br>
  <span class="accent">sociis</span> natoque penatibus et.
</section>

<section class="services">
  <div class="svc" style="left:65px">
    <svg width="70" height="80" viewBox="0 0 70 80"><circle cx="35" cy="22" r="19" fill="#f47b20"/><path d="M2 80c0-22 14-36 33-36s33 14 33 36z" fill="#f47b20"/></svg>
    <h3>Review Candidates<br>Applications</h3><a class="more">View details &rsaquo;</a>
  </div>
  <div class="svc" style="left:258px">
    <svg width="90" height="80" viewBox="0 0 90 80"><ellipse cx="36" cy="30" rx="34" ry="24" fill="#f47b20"/><path d="M18 48l-6 16 18-12z" fill="#f47b20"/><ellipse cx="60" cy="46" rx="28" ry="20" fill="#f47b20" stroke="#0c0c14" stroke-width="4"/><path d="M72 62l8 14-18-10z" fill="#f47b20"/></svg>
    <h3>Interview &amp; Hire</h3><a class="more">View details &rsaquo;</a>
  </div>
  <div class="svc" style="left:453px">
    <svg width="96" height="80" viewBox="0 0 96 80"><circle cx="20" cy="24" r="11" fill="#f47b20"/><circle cx="76" cy="24" r="11" fill="#f47b20"/><circle cx="48" cy="18" r="15" fill="#f47b20"/><path d="M2 62c0-16 8-26 18-26s18 10 18 26zM58 62c0-16 8-26 18-26s18 10 18 26z" fill="#f47b20"/><path d="M24 76c0-24 10-40 24-40s24 16 24 40z" fill="#f47b20" stroke="#0c0c14" stroke-width="3"/></svg>
    <h3>Manage Teams &amp;<br>Payrolls</h3><a class="more">View details &rsaquo;</a>
  </div>
  <div class="hr-block">
    <div class="kicker">This is What We Do</div>
    <h2>Human Resources</h2>
    <p>Aenean commodo ligula eget dolor. Aenean massa. Cum sociis natoque penatibus et magnis dis parturient montes, <span class="accent">nascetur ridiculus</span> mus. Donec quam felis, ultricies nec, pellentesque eu, pretium quis, sem. Nulla <span class="accent">consequat</span> massa quis enim. Donec pede justo, fringilla vel, aliquet nec, vulputate eget, arcu. In enim justo, rhoncus ut, imperdiet a, venenatis vitae, justo. <span class="accent">Aenean commodo</span> ligula eget dolor. Aenean massa. Cum sociis natoque penatibus et magnis dis parturient montes, nascetur ridiculus mus.</p>
  </div>
</section>

<section class="what">
  <h2 class="section-title">WE ARE WHAT WE DO</h2>
  <p class="sub">Why hire use &amp; What we offer</p>
  <div class="badge-art" role="img" aria-label="Ironbark Shift Workforce mascot illustration of a miner in an orange starburst badge"></div>
  <p class="what-text">Aenean <span class="accent">commodo ligula</span> eget dolor. Aenean massa. Cum sociis natoque penatibus et magnis dis parturient montes, nascetur ridiculus mus. Donec quam felis, <span class="accent">ultricies nec</span>, pellentesque eu, pretium quis, <span class="accent">sem</span>.</p>
  <ul class="features" style="left:617px">
    <li>Differenciator Factor</li><li>Differenciator Factor</li><li>Differenciator Factor</li><li>Differenciator Factor</li>
  </ul>
  <ul class="features" style="left:882px">
    <li>Differenciator Factor</li><li>Differenciator Factor</li><li>Differenciator Factor</li><li>Differenciator Factor</li>
  </ul>
  <a class="btn" style="left:617px;width:140px">View all features &nbsp;&rsaquo;</a>
  <a class="btn" style="left:882px;width:140px">Be Hired &nbsp;&rsaquo;</a>
</section>

<section class="projects">
  <h2 class="section-title">Current Projects</h2>
  <p class="sub">Lorem ipsum dolor sit amet</p>
  <p class="lede">Lorem ipsum dolor sit amet, consectetuer adipiscing elit. Aenean commodo ligula eget dolor. Aenean massa. Cum sociis natoque penatibus et magnis dis parturient montes, nascetur ridiculus mus.</p>
  <div class="cards">
    <div class="card"><div class="photo" role="img" aria-label="Aerial photo of a coal stockpile and conveyor site" style="background:linear-gradient(160deg,#a7a49c,#5b5852 60%,#2e2c2a)"></div><h4>Lorem ipsum dolor sit amet,<br>consectetuer adipiscing</h4><div class="links">Detail &rsaquo; &nbsp; Launch &rsaquo;</div></div>
    <div class="card"><div class="photo" role="img" aria-label="Photo of a coal processing plant under blue sky" style="background:linear-gradient(180deg,#3f6fae,#8aa1b8 45%,#4a4740 70%,#262421)"></div><h4>Lorem ipsum dolor sit amet,<br>consectetuer adipiscing</h4><div class="links">Detail &rsaquo; &nbsp; Launch &rsaquo;</div></div>
    <div class="card"><div class="photo" role="img" aria-label="Photo of an open cut mine with terraced walls" style="background:linear-gradient(180deg,#c8cdd2,#9a8a74 45%,#5e4d3b)"></div><h4>Lorem ipsum dolor sit amet,<br>consectetuer adipiscing</h4><div class="links">Detail &rsaquo; &nbsp; Launch &rsaquo;</div></div>
    <div class="card"><div class="photo" role="img" aria-label="Photo of a mine pit with haul trucks" style="background:linear-gradient(180deg,#b9b4a7,#6e6452 50%,#3b342a)"></div><h4>Lorem ipsum dolor sit amet,<br>consectetuer adipiscing</h4><div class="links">Detail &rsaquo; &nbsp; Launch &rsaquo;</div></div>
  </div>
  <div class="dots"><i></i><i></i><i></i><i></i><i></i></div>
</section>

<section class="clients">
  <h2 class="section-title">Clients &amp; Testimonials</h2>
  <p class="sub">Lorem ipsum dolor sit amet, consectetuer adipiscing elit</p>
  <svg class="arrow" style="left:70px" viewBox="0 0 45 45"><rect width="45" height="45" fill="#f47b20"/><path d="M26 14l-9 8.5 9 8.5" stroke="#fff" stroke-width="3" fill="none"/></svg>
  <div class="logos">
    <span>Quarrylink</span><span><i></i>Deepcore</span><span>Shaftwell</span><span><i></i>Basalto</span><span>Pitstone</span>
  </div>
  <svg class="arrow" style="left:1087px" viewBox="0 0 45 45"><rect width="45" height="45" fill="#e4e4e4"/><path d="M19 14l9 8.5-9 8.5" stroke="#fff" stroke-width="3" fill="none"/></svg>
  <p class="quote">Lorem ipsum dolor sit amet, consectetuer adipiscing elit. Aenean commodo ligula eget dolor. Aenean massa.Lorem ipsum dolor sit amet, consectetuer adipiscing elit. Aenean commodo ligula eget dolor. Aenean massa.</p>
  <div class="author"><div class="avatar" role="img" aria-label="Portrait photo of the client"></div><div><b>Callum Reyes</b><small>CEO - Hollin Energy Pty</small></div></div>
</section>

<section class="team">
  <p class="kicker">ABOUT US</p>
  <h2 class="section-title">MEET OUR TEAM</h2>
  <div class="member" style="left:96px"><div class="portrait" role="img" aria-label="Portrait photo of Callum Reyes"></div><h4>CALLUM REYES</h4><p class="role">CEO</p><p>Lorem ipsum dolor sit amet, consectetuer adipiscing elit. Aenean commodo ligula eget dolor. Aenean massa.</p><div class="social"><i class="on"></i><i></i><i></i></div></div>
  <div class="member" style="left:360px"><div class="portrait" role="img" aria-label="Portrait photo of Tessa Marlow"></div><h4>TESSA MARLOW</h4><p class="role">Account Manager</p><p>Lorem ipsum dolor sit amet, consectetuer adipiscing elit. Aenean commodo ligula eget dolor. Aenean massa.</p><div class="social"><i></i><i></i><i></i></div></div>
  <div class="member" style="left:626px"><div class="portrait" role="img" aria-label="Portrait photo of Nadia Okafor"></div><h4>NADIA OKAFOR</h4><p class="role">Financial Chief Executive</p><p>Lorem ipsum dolor sit amet, consectetuer adipiscing elit. Aenean commodo ligula eget dolor. Aenean massa.</p><div class="social"><i></i><i></i><i></i></div></div>
  <div class="member" style="left:890px"><div class="portrait" role="img" aria-label="Portrait photo of Owen Stroud"></div><h4>OWEN STROUD</h4><p class="role">Site Manager</p><p>Lorem ipsum dolor sit amet, consectetuer adipiscing elit. Aenean commodo ligula eget dolor. Aenean massa.</p><div class="social"><i></i><i></i><i></i></div></div>
</section>

<footer class="footer">
  <div class="foot-brand"><i></i>ISW</div>
  <div class="foot-about">
    <p>Lorem ipsum dolor sit amet, consectetuer adipiscing elit. Aenean <span style="color:#3b8fd4">commodo</span> ligula eget dolor. Aenean massa. Cum sociis natoque penatibus et magnis dis parturient <span style="color:#3b8fd4">montes, nascetur</span> ridiculus mus.</p>
    <a class="btn" style="width:132px;margin-top:26px">Read More</a>
  </div>
  <div class="col" style="left:360px">
    <h4>Recent Tweets</h4>
    <div class="tweet"><i></i><div>Lorem ipsum dolor sit amet, consectetuer adipiscing elit. Aenean commodo ligula eget dolor. Aenean massa.<a>22 days ago</a></div></div>
    <div class="tweet"><i></i><div>Lorem ipsum dolor sit amet, consectetuer adipiscing elit. Aenean commodo ligula eget dolor. Aenean massa.<a>3 months 17 days ago</a></div></div>
  </div>
  <div class="col" style="left:661px">
    <h4>Useful Links</h4>
    <ul class="links"><li>My Account</li><li class="active">Resources</li><li>Team</li><li>Current Sites</li><li>News</li><li>Contact</li></ul>
  </div>
  <div class="col contact" style="left:899px">
    <h4>Contact Info</h4>
    <p>Address:<br>42 Seam Road, Moranbah QLD</p>
    <p>Phone number:<br>+61 7 4941 2208, +61 7 4941 2290</p>
    <p>E-mail:<br>hello@ironbarkshift.com.au</p>
    <a class="btn" style="width:132px;margin-top:4px">Get in touch! &nbsp;&#9993;</a>
  </div>
</footer>

<div class="bottom">
  <p class="copy">Copyright © 2013 by ISW . All rights reserved.</p>
  <div class="bottom-links"><a style="left:673px">About</a><a style="left:753px">Login</a><a style="left:828px">Job Application</a><a style="left:960px">News</a><a style="left:1050px">Contact Form</a></div>
  <a class="to-top"><svg width="44" height="33" viewBox="0 0 44 33"><path d="M17 19l5-5 5 5" stroke="#fff" stroke-width="2" fill="none"/></svg></a>
</div>

</body>
</html>
```